C U B A N - C I G A R S - F L Y E R

I need a double-sided 5x7 club type flyer for a Memorial Day Weekend Trip.
The main side design needs to be similar to the attached flyer example. The front design of flyer is KEY. The design will be awarded to the closest finished submission to the example flyer.
Both sides of the flyer should also included event and business logo, which are also attached. Both logos can be altered to fit printing need accordingly.
Front side content is also attached.
The back side design will be very simple. Consists of 3 travel images and trip description, and my contact very details. Same color design as front. The attached word document contains backside details for REFERENCE ONLY. Please focus on front side when submitting a design for this project.
Target Market(s)
A F R I C A N - A M E R I C A N - C I G A R - S M O K E R S
Industry/Entity Type
Travel Industry
Requirements
Must have
- All the elements of the attached information
Nice to have
- Masculine Images
Should not have
- Large Cigar focus to catch customer's attention

```html
<!DOCTYPE html>
<html lang="en">
<head>
<meta charset="utf-8">
<title>Cuba Cigar Gentlemen's Weekend Flyer</title>
<link href="https://fonts.googleapis.com/css2?family=Black+Ops+One&family=Great+Vibes&family=Lato:wght@400;700;900&display=swap" rel="stylesheet">
<style>
  :root{
    --bg:#dcdcdc;
    --navy:#1f2f6b;
    --red:#d8202a;
    --panel:#86a9d6;
    --pink:#ee8e92;
    --pink-light:#f6b3b5;
    --photo-dark:#0f1a33;
    --white:#ffffff;
    --ink:#2a2a2a;
  }
  *{box-sizing:border-box;margin:0;padding:0}
  html,body{width:1200px;height:1200px;overflow:hidden;background:var(--bg);font-family:'Lato',sans-serif}
  .card{position:absolute;left:254px;width:723px;overflow:hidden}
  .front{top:69px;height:515px;background:var(--photo-dark)}
  .back{top:622px;height:514px;background:var(--white)}

  /* front */
  .front-photo{position:absolute;inset:0;background:
      radial-gradient(ellipse 210px 170px at 150px 150px,#e58a8f 0%,#c8707a 55%,transparent 75%),
      radial-gradient(ellipse 200px 120px at 300px 340px,#9fb6d8 0%,#587bb0 50%,transparent 80%),
      linear-gradient(135deg,#1b2b52 0%,#3d5d93 45%,#22355f 75%,#0d1630 100%)}
  .stripe{position:absolute;top:0;height:100%;background:var(--pink)}
  .stripe.l{left:423px;width:12px}
  .stripe.r{left:678px;width:11px}
  .panel{position:absolute;left:435px;top:0;width:243px;height:100%;background:var(--panel);text-align:center}
  .badge{position:absolute;left:61px;top:14px;width:124px;height:124px;border-radius:50%;border:3px solid var(--navy);display:flex;align-items:center;justify-content:center}
  .badge-name{font-weight:900;color:var(--navy);font-size:19px;line-height:1.1;width:90px}
  .head{position:absolute;left:0;width:100%;font-family:'Black Ops One',sans-serif;line-height:1;white-space:nowrap}
  .h-cuba{top:152px;font-size:29px;color:var(--white)}
  .h-gent{top:193px;font-size:25px;color:var(--red)}
  .h-script{position:absolute;top:220px;left:0;width:100%;font-family:'Great Vibes',cursive;font-size:19px;line-height:24px;color:var(--navy);white-space:nowrap}
  .h-script .stars{font-family:'Lato',sans-serif;font-size:8px;vertical-align:middle;letter-spacing:1px}
  .h-legal{position:absolute;top:249px;left:0;width:100%;font-size:12.5px;line-height:15px;color:var(--white);font-weight:700}
  .h-cigars{top:284px;font-size:27px;color:var(--navy)}
  .h-tripname{top:322px;font-size:18px;color:var(--red)}
  .h-tripvalue{position:absolute;top:345px;left:0;width:100%;font-size:17px;color:var(--white);white-space:nowrap}
  .h-weekend{top:379px;font-size:14px;color:var(--navy)}
  .h-weekend span{color:var(--red)}
  .book{position:absolute;left:409px;top:419px;width:294px;height:84px;border:3px solid var(--white);border-radius:12px;background:linear-gradient(180deg,var(--pink-light),var(--pink));text-align:center}
  .book-now{font-weight:700;font-size:33px;color:var(--navy);margin-top:6px;line-height:1}
  .book-now span{color:var(--red)}
  .book-limit{font-family:'Black Ops One',sans-serif;font-size:26px;color:var(--red);line-height:1;margin-top:6px}
  .dates{position:absolute;left:16px;top:413px;font-family:'Black Ops One',sans-serif;font-size:15px;color:var(--white);letter-spacing:.3px;white-space:nowrap}
  .dates-rule{position:absolute;left:0;top:447px;width:270px;height:2px;background:var(--white)}
  .contact-band{position:absolute;left:0;top:449px;width:338px;height:50px;background:rgba(60,100,160,.55)}
  .contact{position:absolute;left:0;top:455px;width:338px;text-align:center;font-size:12.5px;line-height:20px;color:var(--white);font-weight:700;white-space:nowrap}

  /* back */
  .pic{position:absolute;top:16px;width:213px;height:138px}
  .pic-frame{position:absolute;top:22px;width:213px;height:138px}
  .pic.cars{left:28px;background:linear-gradient(160deg,#e33c8c 0%,#f4cf1c 35%,#1f6fd0 70%,#15427f 100%)}
  .pic.map{left:260px;background:radial-gradient(ellipse at 50% 50%,#ffffff 0%,#cfe0f5 100%)}
  .pic.cigars{left:487px;background:linear-gradient(135deg,#8a5430 0%,#5e3419 50%,#9a6538 100%)}
  .frame-blue{left:34px;background:var(--panel)}
  .frame-pink{left:266px;background:var(--pink)}
  .frame-blue2{left:493px;background:var(--panel)}
  .story{position:absolute;left:28px;top:176px;width:678px;font-size:10.4px;line-height:13.8px;color:var(--ink);text-align:justify}
  .col{position:absolute;top:316px;font-size:13.4px;line-height:17.2px;color:var(--ink)}
  .col-1{left:34px;width:190px}
  .col-2{left:256px;width:240px}
  .col-3{left:522px;width:190px}
  .divider{position:absolute;top:322px;width:1px;height:164px;background:#555}
  .label{color:var(--red)}
  .blue{color:#2b5bb5}
  .star{color:var(--red)}
  .strong{font-weight:700}
  .back-band{position:absolute;left:0;bottom:0;width:100%;height:7px;background:var(--panel)}
</style>
</head>
<body>

<section class="card front">
  <div class="front-photo" role="img" aria-label="Photo of a pink fedora hat, a cigar resting in a glass ashtray and a saxophone in dark blue tones"></div>
  <div class="stripe l"></div>
  <div class="panel">
    <div class="badge"><div class="badge-name">Havana Weekend</div></div>
    <div class="head h-cuba">A CUBA CIGAR</div>
    <div class="head h-gent">GENTLEMEN'S</div>
    <div class="h-script"><span class="stars">★★</span> Memorial Day Weekend <span class="stars">★★</span></div>
    <div class="h-legal">Legally travel to Cuba and<br>return with real</div>
    <div class="head h-cigars">CUBAN CIGARS!</div>
    <div class="head h-tripname">Trip Name:</div>
    <div class="h-tripvalue">Rum Cigars and Classic Cars</div>
    <div class="head h-weekend">MEMORIAL DAY WEEKEND <span>2018!</span></div>
  </div>
  <div class="stripe r"></div>
  <div class="dates">FRIDAY, MAY 25TH – TUESDAY MAY 29TH</div>
  <div class="dates-rule"></div>
  <div class="contact-band"></div>
  <div class="contact">Book Today at www.leafandvoyage.com/CUBA2018<br>For More Information Call: XXX-XXX-XXXX</div>
  <div class="book">
    <div class="book-now">Book Now<span>!</span></div>
    <div class="book-limit">SPACE IS LIMITED</div>
  </div>
</section>

<section class="card back">
  <div class="pic-frame frame-blue"></div>
  <div class="pic cars" role="img" aria-label="Photo of colorful classic American cars lined up in Havana"></div>
  <div class="pic-frame frame-pink"></div>
  <div class="pic map" role="img" aria-label="Map of Cuba showing the flight route from Miami to Havana"></div>
  <div class="pic-frame frame-blue2"></div>
  <div class="pic cigars" role="img" aria-label="Close-up photo of a row of Cuban cigars"></div>

  <p class="story">Cuba is the ultimate bucket list destination for any cigar lover. Now is your opportunity to legally travel to Cuba and experience a country that has been off limits to Americans for more than 50 years before it changes. Smoke fine Cuban cigars, meet its resilient people and experience Cuba's fascinating culture. Tour cigar factories, watch expert cigar rollers, visit a humidor factory and work- shop, tour the Malecón Rum Heritage Museum to learn firsthand the process of making rum followed by rum tasting and pairings with Cuban cigars in a private setting and much more. Explore the Pinar Del Rio located in the Viñales Valley known for its stunning land- scapes and tobacco plantations. Visit the world famous Verdeluz Tobacco Plantation to see first hand where and how the tobacco process is grown for fine Cuban Cigars. The bucket list trip of a lifetime awaits on this 'people to people' Cigar Journey to Cuba to learn first hand about Cuban cigars, meet the Cuban people, experience incredible cuisine, drive in classic American cars along the Malecón and experience the Cuban cigar process from seed to smoke' and an opportunity to smoke in the birthplace of cigars!</p>

  <div class="col col-1">
    <span class="label">Trip Cost</span>: $2050<br>
    <span class="label">Deposit</span>: $300<br>
    Payment plans available<br>
    <span class="blue">$300</span> Deposit Required<br>
    Final payment Due By April 10, 2018<br>
    <span class="star">*</span><span class="strong">NON-REFUNDABLE</span><br>
    <span class="star">*</span>Passport Required
  </div>
  <div class="divider" style="left:231px"></div>
  <div class="col col-2">
    What's Included:<br>
    <span class="strong">4 Days / 3 Nights</span><br>
    5 Star Hotel Accommodations Based on Double Occupancy<br>
    Roundtrip Coastal Air Airline Tickets from Fort Lauderdale Florida - Cuba<br>
    Tour Bus Chauffeured Transportation<br>
    All Rum and Cigar Tour Events<br>
    Select Meals (Breakfast, Welcome and Farewell Dinner)<br>
    and More!
  </div>
  <div class="divider" style="left:504px"></div>
  <div class="col col-3">
    <span class="strong">$300</span> Deposit Required<br>
    Final payment Due By April 10, 2018<br>
    <span class="star">*</span><span class="strong">NON-REFUNDABLE</span><br>
    <span class="star">*</span><span class="strong">Passport Required</span>
  </div>
  <div class="back-band"></div>
</section>

</body>
</html>
```